KALO Wave Co.
KALO Wave Co. - Sports
Creative Brief
Sports
www.kalowave.example
Inspired by Neptune, Roman God of the Sea, KALO Wave Co was created to produce the most cutting-edge performance and high quality boards EVER made, period.
With that being said, not everyone is meant to ride a KALO.
KALO Wave Co is a small company created by a group of close friends that LOVE the ocean, especially surfing. Our passion is in our work, and it shows in our ideas.
We want to portray the lifestyle of a true surfer: strapping their board on top of their jalopy, setting out for the unexplored coastline, and finding THE spot of their own.
Likes: Background dark in color (Feel of sunset over ocean) soft white writing. Image of surfer popping off wake on board Image of surfers *male and female having a good time (smiling, etc.) Dislike: Cookie-cutter templates
Black
Sunset Orange
Soft White
top
http://www.brimtrek.example/shop/us/en/ (background image)
http://www.dashfen.example/#/women/americacanada/teamriders/r.surf|marla_quenby (feel)
http://www.glowtrove.example/images/Waterfront%20at%20Night.jpg (photo lighting)
Edgy Cool Sexy Energy Tabs across top to include: Products, Technology, About Us, What's New, Contact Us Need good balance. Similar point of view of Tidelark/Brackenfoam/Gumbaroo Possible quote in small font "Life's too short to be ordinary" Would like to add small social network icons on lower right.

```html
<!DOCTYPE html>
<html lang="en">
<head>
<meta charset="utf-8">
<title>KALO Wave Co.</title>
<link rel="stylesheet" href="https://fonts.googleapis.com/css2?family=Arimo:wght@400;700&family=Lora:ital,wght@0,700;1,400&family=Permanent+Marker&display=swap">
<style>
:root{
  --black:#0b0b0b;
  --ink:#1a1a1a;
  --sunset:#f28a1a;
  --soft-white:#f4f2ee;
  --paper:#ffffff;
  --grey:#8a8a8a;
  --sea-deep:#0e2c4a;
  --sea:#2f6f9c;
  --sky:#9cc3dc;
}
*{margin:0;padding:0;box-sizing:border-box}
html,body{width:1200px;height:809px;overflow:hidden;background:var(--black)}
.page{position:relative;width:1200px;height:809px;background:var(--black);font-family:"Arimo",Arial,sans-serif;color:var(--soft-white)}
.hero{position:absolute;left:0;top:0;width:1200px;height:470px;
  background:radial-gradient(ellipse at 60% 40%,rgba(0,0,0,0) 30%,rgba(0,0,0,.75) 85%),
  linear-gradient(180deg,var(--sky) 0%,var(--sea) 32%,#5f9cc0 52%,var(--sea-deep) 100%)}
.brand{position:absolute;left:120px;top:12px;width:264px;height:120px;background:var(--black);display:flex;align-items:center;gap:16px;padding-left:22px}
.brand-mark{width:50px;height:50px;border-radius:50%;background:var(--sunset);flex:none}
.brand-name{font-weight:700;font-size:30px;color:var(--soft-white);letter-spacing:.5px}
.nav{position:absolute;top:36px;left:427px;display:flex;gap:0}
.nav a{color:var(--soft-white);text-decoration:none;font-weight:700;font-size:17px;position:relative;padding:0 13px}
.nav a.current{color:var(--sunset)}
.nav a.current::before{content:"";position:absolute;left:0;right:0;top:-8px;bottom:-8px;background:var(--soft-white);border-radius:40% 60% 50% 45%;transform:skew(-12deg);z-index:-1}
.nav a.current{z-index:1}
.tagline{position:absolute;left:132px;top:380px;font-family:"Permanent Marker",cursive;font-size:38px;color:var(--soft-white);letter-spacing:1px}
.band{position:absolute;left:0;top:450px;width:1200px;height:290px}
.band svg{position:absolute;left:0;top:0}
.about{position:absolute;left:130px;top:485px;width:470px;color:var(--ink)}
.products{position:absolute;left:626px;top:485px;width:515px;color:var(--ink)}
.section-title{display:flex;align-items:center;gap:9px;font-weight:700;font-size:17px;text-transform:uppercase;padding-bottom:12px;border-bottom:1px solid #d4d4d4}
.section-title::before{content:"";width:16px;height:16px;border-radius:50%;background:var(--ink)}
.about p{font-family:"Lora",Georgia,serif;font-style:italic;font-size:14.5px;line-height:19px;margin-top:14px}
.read-more{display:inline-block;margin-top:14px;font-family:"Lora",Georgia,serif;font-weight:700;font-size:16px;color:var(--ink);text-decoration:none;border-bottom:2px solid var(--ink)}
.carousel{display:flex;align-items:center;margin-top:22px;gap:10px}
.arrow{width:22px;height:22px;border-radius:50%;border:2px solid #9a9a9a;flex:none;display:flex;align-items:center;justify-content:center}
.items{display:flex;gap:26px;margin:0 14px}
.item{width:90px;font-size:12px;font-weight:700;color:#3a3a3a}
.thumb{display:block;width:90px;height:68px;border:2px solid #cfcfcf;margin-bottom:6px}
.item.active .thumb{border-color:var(--sunset)}
.t-boards{background:linear-gradient(160deg,#6b7c86,#20262b)}
.t-fins{background:linear-gradient(160deg,#f4f4f4,#7a7a7a)}
.t-suits{background:linear-gradient(160deg,#e9e9e9,#3a3f52)}
.t-shirts{background:linear-gradient(160deg,#efefef,#2a2a2a)}
.view-all{display:inline-block;margin:18px 0 0 46px;font-size:12px;color:var(--sunset);text-decoration:underline}
.footer{position:absolute;left:132px;top:746px;width:936px}
.footer-nav{display:flex;gap:16px}
.footer-nav a{color:var(--soft-white);text-decoration:none;font-size:12.5px}
.copyright{margin-top:10px;font-size:11.5px;color:#cfcfcf}
.social{position:absolute;right:0;top:2px;display:flex;gap:12px}
.social span{width:34px;height:34px;border-radius:4px;background:#6f6f6f}
</style>
</head>
<body>
<div class="page">
  <div class="hero" role="img" aria-label="Surfer couple seen from behind carrying a board toward a blue ocean with breaking waves"></div>

  <div class="brand"><span class="brand-mark"></span><span class="brand-name">KALO Wave Co.</span></div>

  <nav class="nav">
    <a href="#">Home</a>
    <a href="#" class="current">About Us</a>
    <a href="#">Products</a>
    <a href="#">Technology</a>
    <a href="#">What's New</a>
    <a href="#">Contact Us</a>
  </nav>

  <h1 class="tagline">LIFE'S TOO SHORT TO BE ORDINARY</h1>

  <div class="band">
    <svg width="1200" height="290" viewBox="0 0 1200 290">
      <polygon fill="#ffffff" points="0,12 60,4 110,14 170,2 240,10 300,0 360,12 430,3 500,13 560,5 630,14 700,2 770,11 840,4 900,13 970,1 1040,10 1100,3 1160,12 1200,5 1200,272 1150,282 1080,270 1010,284 940,272 870,286 800,274 730,283 660,270 590,285 520,273 450,284 380,271 310,286 240,274 170,283 100,271 40,284 0,276"/>
    </svg>
  </div>

  <section class="about">
    <h2 class="section-title">Who we are</h2>
    <p>KALO Wave Co is a small company created by a group of close friends that LOVE the ocean, especially surfing. Our passion is in our work, and it shows in our ideas.</p>
    <p>We want to portray the lifestyle of a true surfer: strapping their board on top of their jalopy, setting out for the unexplored coastline, and finding THE spot of their own.</p>
    <a href="#" class="read-more">Read More</a>
  </section>

  <section class="products">
    <h2 class="section-title">Summer 2011 Products</h2>
    <div class="carousel">
      <span class="arrow"><svg width="10" height="10" viewBox="0 0 10 10"><polygon points="7,1 2,5 7,9" fill="#9a9a9a"/></svg></span>
      <div class="items">
        <div class="item"><span class="thumb t-boards" role="img" aria-label="Surfboard product photo"></span>Boards</div>
        <div class="item active"><span class="thumb t-fins" role="img" aria-label="Surf fin product photo"></span>Fins</div>
        <div class="item"><span class="thumb t-suits" role="img" aria-label="Swimsuit product photo"></span>Suits</div>
        <div class="item"><span class="thumb t-shirts" role="img" aria-label="T-shirt product photo"></span>T-Shirts</div>
      </div>
      <span class="arrow"><svg width="10" height="10" viewBox="0 0 10 10"><polygon points="3,1 8,5 3,9" fill="#9a9a9a"/></svg></span>
    </div>
    <a href="#" class="view-all">View all summer products</a>
  </section>

  <footer class="footer">
    <nav class="footer-nav">
      <a href="#">Home</a><a href="#">About Us</a><a href="#">Products</a><a href="#">Technology</a><a href="#">What's New</a><a href="#">Contact Us</a>
    </nav>
    <p class="copyright">© 2011, KALO Wave Co. All rights Reserved</p>
    <div class="social"><span></span><span></span><span></span><span></span></div>
  </footer>
</div>
</body>
</html>
```